Promotional poster for a vintage motorcycle show.

Vertically oriented, based on 11 x 17 inch proportions

Though not to the exclusion of other design concepts, stylistically perhaps something evoking a vintage (early-mid 20th century) 2-3 color silk screen style event poster.

In addition to some sort of eyecatching, vintage / antique motorbike oriented graphic (preferably not Corwin Baxley based), the poster should include the following text and info:

3rd Annual Milo Quenby Vintage Motorcycle Show
Bordentown City, N.J.
October 1st (rain date Oct. 2nd)
11am-4pm

Presented in conjunction with the 27th Annual Thistlewood Fair

For further info, or to register your pre-1992 bike contact:
Marty@wheelvaultex.com or 555-204-8913

Sponsored by:
UptownHallowmereGuildway.com
Wheelvaultex.com

Must have
• See above project description
Nice to have
• See above project describtion

```html
<!DOCTYPE html>
<html lang="en">
<head>
<meta charset="utf-8">
<title>3rd Annual Milo Quenby Vintage Motorcycle Show</title>
<link rel="stylesheet" href="https://fonts.googleapis.com/css2?family=Josefin+Sans:wght@400;600&display=swap">
<style>
  :root {
    --paper-light: #ece6de;
    --paper-mid: #ddd4c9;
    --paper-dark: #cfc4b7;
    --ink: #1f1c1a;
    --ribbon: #2f2b27;
    --ribbon-text: #d8c6b3;
    --rule: #5a5550;
  }
  html, body { margin: 0; padding: 0; overflow: hidden; }
  body { width: 764px; height: 1200px; }
  .poster {
    position: relative;
    width: 764px;
    height: 1200px;
    overflow: hidden;
    background: radial-gradient(ellipse at 40% 35%, var(--paper-light) 0%, var(--paper-mid) 60%, var(--paper-dark) 100%);
    color: var(--ink);
    font-family: "Josefin Sans", sans-serif;
    font-weight: 600;
    text-transform: uppercase;
  }
  .frame-outer, .frame-inner {
    position: absolute;
    border: 1.5px solid var(--ink);
    pointer-events: none;
  }
  .frame-outer { inset: 14px; }
  .frame-inner { inset: 20px; border-width: 1px; }
  .line {
    position: absolute;
    left: 0; right: 0;
    text-align: center;
    line-height: 1;
    white-space: nowrap;
    margin: 0;
  }
  .dotted-rule {
    position: absolute;
    left: 206px; width: 370px;
    border-top: 2px dotted var(--ink);
  }
  .edition { top: 102px; font-size: 40px; letter-spacing: 1px; }
  .ribbon { position: absolute; left: 0; top: 156px; }
  .ribbon-title { top: 174px; font-size: 54px; color: var(--ribbon-text); letter-spacing: 1px; }
  .show-name { top: 248px; font-size: 39px; letter-spacing: 0.5px; }
  .location { top: 318px; font-size: 24px; font-weight: 400; }
  .date { top: 358px; font-size: 24px; font-weight: 400; }
  .hours { top: 394px; font-size: 24px; font-weight: 400; }
  .hours-rule {
    position: absolute; top: 405px; width: 66px;
    border-top: 2px solid var(--ink);
  }
  .hours-rule.left { left: 206px; }
  .hours-rule.right { left: 498px; }
  .bike-art {
    position: absolute;
    left: 68px; top: 448px;
    width: 652px; height: 244px;
    background: radial-gradient(ellipse at center, rgba(31,28,26,0.22) 0%, rgba(31,28,26,0.08) 60%, rgba(31,28,26,0) 100%);
  }
  .presented { top: 756px; font-size: 19px; font-weight: 600; }
  .fair { top: 788px; font-size: 27px; font-weight: 600; }
  .divider { position: absolute; left: 0; }
  .contact-intro { top: 886px; font-size: 15.5px; font-weight: 400; letter-spacing: 0.3px; }
  .contact { font-size: 29px; font-weight: 400; }
  .email { top: 914px; text-transform: uppercase; }
  .phone { top: 952px; }
  .sponsor-label { top: 1050px; font-size: 19px; font-weight: 400; }
  .sponsor { font-size: 20px; font-weight: 400; letter-spacing: 0.5px; }
  .sponsor.first { top: 1084px; }
  .sponsor.second { top: 1122px; }
</style>
</head>
<body>
<main class="poster">
  <div class="frame-outer"></div>
  <div class="frame-inner"></div>

  <div class="dotted-rule" style="top:86px"></div>
  <p class="line edition">3rd Annual</p>
  <div class="dotted-rule" style="top:146px"></div>

  <svg class="ribbon" width="764" height="86" viewBox="0 0 764 86" aria-hidden="true">
    <polygon points="120,0 656,0 630,42 656,84 120,84 146,42" fill="var(--ribbon)"/>
  </svg>
  <h1 class="line ribbon-title" style="font-weight:600">Milo Quenby</h1>
  <h2 class="line show-name" style="font-weight:600">Vintage Motorcycle Show</h2>

  <p class="line location">Bordentown City, N.J.</p>
  <p class="line date">October 1st (Rain Date Oct. 2nd)</p>
  <div class="hours-rule left"></div>
  <p class="line hours">11am-4pm</p>
  <div class="hours-rule right"></div>

  <div class="bike-art" role="img" aria-label="Line-art illustration of a vintage motorcycle in side view"></div>

  <p class="line presented">Presented in conjunction with the</p>
  <p class="line fair">27th Annual Thistlewood Fair</p>

  <svg class="divider" style="top:832px" width="764" height="16" viewBox="0 0 764 16" aria-hidden="true">
    <g stroke="var(--rule)" stroke-width="1.5" fill="none">
      <line x1="150" y1="8" x2="332" y2="8"/>
      <line x1="432" y1="8" x2="630" y2="8"/>
      <polyline points="158,3 150,8 158,13"/>
      <polyline points="165,3 157,8 165,13"/>
      <polyline points="622,3 630,8 622,13"/>
      <polyline points="615,3 623,8 615,13"/>
    </g>
    <g fill="var(--rule)">
      <circle cx="350" cy="8" r="1.6"/><circle cx="366" cy="8" r="1.6"/><circle cx="382" cy="8" r="1.6"/>
      <circle cx="398" cy="8" r="1.6"/><circle cx="414" cy="8" r="1.6"/>
    </g>
  </svg>

  <p class="line contact-intro">For further info, or to register your pre-1992 bike contact:</p>
  <p class="line contact email">Marty@wheelvaultex.com</p>
  <p class="line contact phone">or 555-204-8913</p>

  <svg class="divider" style="top:996px" width="764" height="16" viewBox="0 0 764 16" aria-hidden="true">
    <g stroke="var(--rule)" stroke-width="1.5" fill="none">
      <line x1="150" y1="8" x2="332" y2="8"/>
      <line x1="432" y1="8" x2="630" y2="8"/>
      <polyline points="158,3 150,8 158,13"/>
      <polyline points="165,3 157,8 165,13"/>
      <polyline points="622,3 630,8 622,13"/>
      <polyline points="615,3 623,8 615,13"/>
    </g>
    <g fill="var(--rule)">
      <circle cx="350" cy="8" r="1.6"/><circle cx="366" cy="8" r="1.6"/><circle cx="382" cy="8" r="1.6"/>
      <circle cx="398" cy="8" r="1.6"/><circle cx="414" cy="8" r="1.6"/>
    </g>
  </svg>

  <p class="line sponsor-label">Sponsored by:</p>
  <p class="line sponsor first">UptownHallowmereGuildway.com</p>
  <p class="line sponsor second">Wheelvaultex.com</p>
</main>
</body>
</html>
```